Business Card Design For Office Furniture Clearance Company

Kestrel Office Clearance - our company name pretty much explains what we do, we clear offices for high end clients, mainly plc's and large international companies.

We require a nice looking business card that displays professionalism but without being too serious.

It would be nice to see just a little more than a conventional boring business card, make sure you add some flare.

Industry/Entity Type

Office Furniture

Contact Information for Business Card

CARD 1

Tom Pardew
Director
tom@kestrelofficeclearance.co.uk
m: 07700 513928

t: 01632 419063
www.kestrelofficeclearance.co.uk

Kestrel Office Clearance
Unit K4 B
3-7 Ferndale Lane
Ashcombe
Harrowfield
ZZ9 4QX

free office clearances… you cant get better than that.

CARD 2

Henry Walbrook
Director
henry@kestrelofficeclearance.co.uk
m: 07700 628157

t: 01632 419063

Kestrel Office Clearance
Unit K4 B
3-7 Ferndale Lane
Ashcombe
Harrowfield
ZZ9 4QX

Font styles to use
Sans Serif

Requirements
Must have
• A white background - as we have a blue logo.
Nice to have
• Nice use of the logo - play around with this and dissect it.

```html
<!DOCTYPE html>
<html lang="en">
<head>
<meta charset="utf-8">
<title>Kestrel Office Clearance – Business Cards</title>
<link rel="stylesheet" href="https://fonts.googleapis.com/css2?family=Barlow:wght@300;400;500&display=swap">
<style>
  :root {
    --page: #d9dadc;
    --blue-deep: #0b5a92;
    --blue-core: #0f70b3;
    --blue-mid: #4a9bcb;
    --blue-light: #8fc0de;
    --blue-mist: #e6f0f7;
    --white: #ffffff;
    --ink: #1c2128;
    --ink-soft: #4d5965;
    --font: "Barlow", Arial, sans-serif;
  }
  * { box-sizing: border-box; margin: 0; padding: 0; }
  html, body {
    width: 1200px; height: 786px; overflow: hidden;
    background: var(--page);
    font-family: var(--font);
  }
  .sheet {
    width: 1200px; height: 786px;
    display: grid;
    grid-template-columns: 500px 500px;
    grid-template-rows: 324px 324px;
    gap: 58px 80px;
    justify-content: center;
    align-content: center;
  }
  .card {
    width: 500px; height: 324px;
    position: relative; overflow: hidden;
    box-shadow: 0 6px 18px rgba(0,0,0,.18);
  }
  .front-art {
    position: absolute; inset: 0;
    background: linear-gradient(135deg, var(--blue-deep) 0%, var(--blue-mid) 45%, var(--blue-light) 70%, var(--blue-core) 100%);
  }
  .brand-badge {
    position: absolute;
    left: 140px; top: 60px;
    width: 200px; height: 200px;
    border-radius: 50%;
    background: var(--blue-core);
    display: flex; flex-direction: column;
    align-items: center; justify-content: center;
    color: var(--white);
    font-weight: 500;
    text-align: center;
    line-height: 1.2;
  }
  .brand-badge .brand-line-1 { font-size: 26px; }
  .brand-badge .brand-line-2 { font-size: 17px; }
  .card-back { background: var(--white); }
  .back-circle {
    position: absolute;
    left: 82px; top: 40px;
    width: 190px; height: 190px;
    border-radius: 50%;
    background: var(--blue-mist);
  }
  .details {
    position: absolute;
    left: 138px; top: 58px;
    color: var(--ink);
    line-height: 1.25;
  }
  .person-name { font-size: 24px; font-weight: 400; letter-spacing: .3px; padding-left: 64px; }
  .person-role { font-size: 15px; font-weight: 400; padding-left: 100px; margin-bottom: 8px; }
  .contact-line { font-size: 15.5px; font-weight: 400; }
  .contact-line span + span { margin-left: 10px; }
  .address {
    margin-top: 14px;
    font-size: 12px; font-weight: 300;
    color: var(--ink-soft);
    line-height: 1.35;
  }
</style>
</head>
<body>
<main class="sheet">

  <section class="card card-front" aria-label="Card front, Henry Walbrook">
    <div class="front-art" role="img" aria-label="Angular blue geometric background artwork"></div>
    <div class="brand-badge">
      <span class="brand-line-1">Kestrel</span>
      <span class="brand-line-2">Office Clearance</span>
    </div>
  </section>

  <section class="card card-front" aria-label="Card front, Tom Pardew">
    <div class="front-art" role="img" aria-label="Angular blue geometric background artwork"></div>
    <div class="brand-badge">
      <span class="brand-line-1">Kestrel</span>
      <span class="brand-line-2">Office Clearance</span>
    </div>
  </section>

  <section class="card card-back">
    <div class="back-circle"></div>
    <div class="details">
      <p class="person-name">Henry Walbrook</p>
      <p class="person-role">Director</p>
      <p class="contact-line"><span>m: 07700 628157</span><span>t: 01632 419063</span></p>
      <p class="contact-line">www.kestrelofficeclearance.co.uk</p>
      <p class="contact-line">henry@kestrelofficeclearance.co.uk</p>
      <p class="address">Kestrel Office Clearance, Unit K4 B 3-7 Ferndale Lane, Ashcombe<br>Harrowfield, ZZ9 4QX</p>
    </div>
  </section>

  <section class="card card-back">
    <div class="back-circle"></div>
    <div class="details">
      <p class="person-name">Tom Pardew</p>
      <p class="person-role">Director</p>
      <p class="contact-line"><span>m: 07700 513928</span><span>t: 01632 419063</span></p>
      <p class="contact-line">www.kestrelofficeclearance.co.uk</p>
      <p class="contact-line">tom@kestrelofficeclearance.co.uk</p>
      <p class="address">Kestrel Office Clearance, Unit K4 B 3-7 Ferndale Lane, Ashcombe<br>Harrowfield, ZZ9 4QX</p>
    </div>
  </section>

</main>
</body>
</html>
```